Website that informs user about the Darknet

A short 1 pager website that explains what the darknet is.
Current site: https://velmora.gs/ & https://quintable.kr/. No logo needed. Just an informational page. Choose the layout / colours that you prefer.

Target Market(s)

Endusers, companies etc.

Coding

Coded - Design and coding required

Number of Pages Required

1 page

Requirements
Must have
• 1 Small contact form - thats all
Should not have
• The page must look professional. Not for kids. I target mainly adults / employees

```html
<!DOCTYPE html>
<html lang="en">
<head>
<meta charset="utf-8">
<title>Velmora - Cyber Threat Intelligence · Darknet and Darkweb</title>
<link rel="stylesheet" href="https://fonts.googleapis.com/css2?family=Montserrat:wght@300;400;500;600;700;800&display=swap">
<style>
  :root {
    --bg: #000000;
    --text: #c4c4c4;
    --text-soft: #a8a8a8;
    --heading: #e4e4e4;
    --white: #ffffff;
    --accent: #7e0e0e;
    --link: #b01212;
    --rule: #8c8c8c;
    --field-line: #6a6a6a;
    --title-dark: #1c1c1c;
    --title-light: #8f8f8f;
  }
  * { margin: 0; padding: 0; box-sizing: border-box; }
  html, body { width: 1200px; height: 3706px; overflow: hidden; }
  body {
    position: relative;
    background: var(--bg);
    color: var(--text);
    font-family: "Montserrat", Arial, sans-serif;
    font-weight: 300;
    font-size: 14.5px;
    letter-spacing: -0.15px;
    line-height: 18.7px;
  }
  .abs { position: absolute; }
  .lines { white-space: nowrap; }

  .site-name { left: 78px; top: 72px; font-size: 15px; font-weight: 400; letter-spacing: 0; color: var(--text); }
  .nav-contact { left: 981px; top: 72px; font-size: 15px; font-weight: 600; letter-spacing: 0; color: var(--white); text-decoration: none; }

  .hero-figure {
    left: 137px; top: 151px; width: 309px; height: 381px;
    background: radial-gradient(ellipse 45% 55% at 52% 45%, #2e2e2e 0%, #161616 45%, #000 80%);
  }
  .hero-title {
    left: 552px; top: 262px; font-size: 84px; font-weight: 800; letter-spacing: -1px; line-height: 96px;
    background: linear-gradient(90deg, var(--title-dark) 0%, var(--title-light) 45%, #9a9a9a 100%);
    -webkit-background-clip: text; background-clip: text; color: transparent;
  }
  .hero-subtitle { left: 554px; top: 366px; font-size: 37px; font-weight: 300; letter-spacing: 0; color: var(--accent); line-height: 40px; }

  .intro { left: 0; width: 1200px; top: 672px; text-align: center; }

  .binary-rain-right {
    left: 1066px; top: 705px; width: 134px; height: 720px;
    background: linear-gradient(180deg, rgba(90,90,90,0.45), rgba(60,60,60,0.25) 60%, rgba(0,0,0,0));
    -webkit-mask: repeating-linear-gradient(90deg, #000 0 14px, transparent 14px 26px);
    mask: repeating-linear-gradient(90deg, #000 0 14px, transparent 14px 26px);
  }
  .binary-rain-left {
    left: 0; top: 3252px; width: 302px; height: 454px;
    background: linear-gradient(0deg, rgba(90,90,90,0.5), rgba(50,50,50,0.25) 65%, rgba(0,0,0,0));
    -webkit-mask: repeating-linear-gradient(90deg, #000 0 14px, transparent 14px 28px);
    mask: repeating-linear-gradient(90deg, #000 0 14px, transparent 14px 28px);
  }

  .section-heading { font-size: 25px; font-weight: 600; color: var(--heading); letter-spacing: 0.5px; line-height: 30px; white-space: nowrap; }
  .copy p + p { margin-top: 18.7px; }
  .onion-link { color: var(--link); text-decoration: none; }

  .what-heading { left: 163px; top: 842px; }
  .what-copy { left: 163px; top: 900px; }
  .illegal-heading { left: 162px; top: 1245px; }
  .illegal-copy { left: 163px; top: 1303px; }

  .monitor-heading { left: 0; width: 1200px; top: 1547px; text-align: center; }
  .monitor-lead { left: 165px; top: 1660px; }
  .monitor-copy { left: 165px; top: 1752px; }

  .column-title { font-size: 14.5px; font-weight: 300; margin-bottom: 34px; }
  .column p + p { margin-top: 18.7px; }
  .col-how { left: 165px; top: 1996px; }
  .col-features { left: 649px; top: 1997px; }
  .column-rule { left: 598px; top: 2000px; width: 2px; height: 331px; background: var(--rule); }

  .suit-figure {
    left: 187px; top: 2468px; width: 245px; height: 374px;
    background: radial-gradient(ellipse 55% 50% at 50% 45%, #4a4a4a 0%, #232323 45%, #000 85%);
  }
  .why-heading { left: 496px; top: 2421px; font-size: 21px; font-weight: 600; letter-spacing: 0.2px; color: var(--heading); white-space: nowrap; }
  .why-copy { left: 496px; top: 2493px; }
  .why-list-title { left: 496px; top: 2643px; }
  .why-list { left: 496px; top: 2680px; list-style: none; }
  .why-list li::before { content: "-"; display: inline-block; width: 23px; }

  .benefits-heading { left: 0; width: 1200px; top: 2935px; text-align: center; font-size: 26px; font-weight: 500; letter-spacing: 0.5px; color: var(--heading); }
  .benefits-copy { left: 0; width: 1200px; top: 3068px; text-align: center; }

  .btn-more {
    left: 436px; top: 3336px; width: 193px; height: 57px;
    border: 2px solid var(--rule); color: var(--text-soft); font-size: 15px; letter-spacing: 0;
    display: flex; align-items: center; justify-content: center; text-decoration: none;
  }
  .btn-contact { left: 679px; top: 3355px; font-size: 15px; font-weight: 600; letter-spacing: 0; color: var(--white); text-decoration: none; }

  .contact-form {
    left: 300px; top: 3420px; width: 600px; height: 32px;
    display: flex; gap: 12px; align-items: stretch;
  }
  .contact-form .field {
    flex: 1; min-width: 0; background: transparent; border: 0; border-bottom: 1px solid var(--field-line);
    color: var(--text); font: 300 13px "Montserrat", Arial, sans-serif; padding: 0 4px; outline: none;
  }
  .contact-form .field::placeholder { color: #7a7a7a; }
  .contact-form .field-message { flex: 1.6; }
  .contact-form .send {
    width: 84px; background: transparent; border: 1px solid var(--rule); color: var(--text-soft);
    font: 400 13px "Montserrat", Arial, sans-serif; cursor: pointer;
  }

  .social-dot { left: 583px; top: 3494px; width: 34px; height: 34px; border-radius: 50%; background: #e6e6e6; display: block; }
  .copyright { left: 0; width: 1200px; top: 3580px; text-align: center; font-size: 13px; letter-spacing: 0; }
  .tagline { left: 0; width: 1200px; top: 3611px; text-align: center; font-size: 12px; letter-spacing: 0; }
</style>
</head>
<body>
  <header>
    <div class="abs site-name">Velmora - Cyber Threat Intelligence</div>
    <a class="abs nav-contact" href="#contact">Contact Us</a>
  </header>

  <div class="abs hero-figure" role="img" aria-label="Photo of a hooded figure in darkness"></div>
  <h1 class="abs hero-title">DARKNET</h1>
  <div class="abs hero-subtitle">AND DARKWEB</div>

  <p class="abs intro">The Dark Web is also referred to as the Darknet. Both terms stand for the same concept.<br>To understand the darknet, we must first explain the Internet.</p>

  <div class="abs binary-rain-right" role="img" aria-label="Falling binary digits decoration"></div>

  <h2 class="abs section-heading what-heading">WHAT IS THE DARKNET</h2>
  <div class="abs copy lines what-copy">
    <p>The Darknet is similar to the Internet, but there are significant differences. Similar to the Internet, the Darknet is only<br>a network of computers (servers) that are connected to each other. Unlike the Internet, however, you can't access the<br>websites with a regular web browser, for example, but with special software like the Nyx Browser. This browser can be<br>installed as an app on the PC or mobile device and access to the darknet is achieved within a few minutes.</p>
    <p>The special thing about software like the Nyx Browser, however, is that communication to the server runs completely<br>encrypted over many other PCs. Everything is encrypted - even the IP address of the systems you are communicating<br>with. Because the connection runs over many PCs, you don't know on which server the website you are accessing<br>is located. Therefore, websites can be operated completely anonymously. In contrast to domains on the Internet,<br>the websites also use much more cryptic names. For example, a darknet does not end in .com or similar, but in .onion.</p>
    <p>Here is an example of a darknet domain (search engine) that can be accessed in the Nyx browser :<br><a class="onion-link" href="#">http://velmoraq7xkt3ndp4wzfhy2lcuo6vbea5mjrs8gikt2qnofw7dxplh.onion/</a></p>
  </div>

  <h2 class="abs section-heading illegal-heading">IS THE DARKNET ILLEGAL?</h2>
  <div class="abs copy lines illegal-copy">
    <p>Many think the darknet and access is crinimell. But this is not the case. The idea of the darknet comes from the desire<br>to create anonymity. Therefore, the darknet makes sense for the exchange of protected business information or<br>communication of political activists. Unfortunately, only criminal elements also seek anonymity. For example, anyone<br>can upload a website completely anonymously to sell drugs or stolen business data. Thanks to anonymous means<br>of payment such as Corvacoin, such business processes can also run smoothly. &nbsp;&nbsp;Both the dark web and the deep web<br>cannot be found in search engine results, or only with great difficulty.</p>
  </div>

  <h2 class="abs section-heading monitor-heading">WHY AND HOW CAN THE DARKNET BE MONITORED?</h2>
  <p class="abs lines monitor-lead">The dark web can be a scary place. Especially if you're new to it and are not properly equipped with all you need<br>to scour safely.</p>
  <div class="abs copy lines monitor-copy">
    <p>Dark web monitoring refers to the process by which you can search, track, or monitor the information regarding your<br>organization on the dark web. With the right tools on the dark web, you can track lost, stolen, or leaked information<br>such as intellectual property, compromised passwords, breached credentials, leaked organization's sensitive data, etc.<br>Oftentimes, these sensitive information are usually transacted among unscrupulous characters in the dark web.<br>With proper dark web monitoring tools, you can better detect threats and dangers on the dark web, which is a step<br>further than just anti-virus, anti-malware programs, and programs that help in identity theft monitoring. In the case of<br>these anti-malware and antivirus programs, they help you monitor and prevent any malicious code aimed at stealing<br>information. However, they do very little in situations, where the deed has already been done.</p>
  </div>

  <div class="abs column lines col-how">
    <h3 class="column-title">How does dark web monitoring work?</h3>
    <p>When you utilize these dark web monitoring tools,<br>there is a constant search for stolen, lost, or leaked<br>information in the dark web, in real time. Millions of<br>sites all over the dark are searched simultaneously<br>for specific information like email addresses of the<br>corporation, or general information like the name<br>of the company or industry you operate in.</p>
    <p>When any impending threat or loss of information is<br>found, you will receive an alert which can be<br>customized by you. This alert notifies just about<br>anyone or any team relevant to the threat like the<br>legal, marketing, fraud teams, or even human<br>resources.</p>
  </div>
  <div class="abs column-rule"></div>
  <div class="abs column lines col-features">
    <h3 class="column-title">Features found in dark web monitoring</h3>
    <p>1. Threat intelligence When the darknet monitoring service<br>receives data matching the search terms, this data is<br>automatically forwarded to the CISO or a SOC (Security<br>Operations Center).</p>
    <p>2. Threat hunting For individuals who are considered threat<br>hunters, monitoring the dark web can help speed up their<br>search and give them a more complete picture of the danger<br>and nature of a potential threat. This can help prevent<br>phishing or ransomware attacks, for example.</p>
    <p>3. Quicker incidence response &nbsp;With quicker responses to<br>incidences of threat and danger, there will be faster threat<br>mitigation.</p>
  </div>

  <div class="abs suit-figure" role="img" aria-label="Photo of a man in a dark suit and tie, face out of frame"></div>
  <h2 class="abs why-heading">Why should you use dark web monitoring?</h2>
  <p class="abs lines why-copy">On the dark web, there are a lot of things to worry about. Apart from lost credentials,<br>dark web monitoring can also reveal chatter or activity around a business or<br>company that has been attacked, is under attack, or reveal any impending attack.<br>Using this service, you can classify or rank risks from unknown sources in order of<br>severity, and businesses can use this classification to identify and mitigate dangers<br>quicker. &nbsp;Some of those risks include ;</p>
  <p class="abs lines why-list-title">Data dumps to criminal chatrooms or hackers forum</p>
  <ul class="abs lines why-list">
    <li>Third party breaches</li>
    <li>P2P leaks</li>
    <li>Brand misuse</li>
    <li>Accidental leaks</li>
    <li>Domain spoofing</li>
    <li>Impersonations</li>
    <li>Potential threats</li>
  </ul>

  <h2 class="abs benefits-heading">Benefits of Dark Web Monitoring</h2>
  <div class="abs copy lines benefits-copy">
    <p>Dark web monitoring affords you with the ability to track leaked data and the time it has spent released. Actively monitoring<br>the dark web with these tools, give cybercriminals less time to execute attacks and leak sensitive information. &nbsp;&nbsp;Additionally,<br>businesses that monitor the dark web can find out if a breach is imminent, or if they are likely to be breached. If a breach does<br>happen, it will give them an insight as to who is leading the attack and what method of attack is being employed.</p>
    <p>Who needs dark web monitoring tools? Simply put, everybody. These services are important to businesses or individuals<br>whose job is to protect the online presence of other businesses. It is also for businesses with valuable intellectual or sensitive<br>information that may be a target to cybercriminals.</p>
  </div>

  <div class="abs binary-rain-left" role="img" aria-label="Falling binary digits decoration"></div>

  <a class="abs btn-more" href="#">Find Ourt More</a>
  <a class="abs btn-contact" href="#contact">Contact Us</a>

  <form class="abs contact-form" id="contact" action="#" method="post" aria-label="Contact form">
    <input class="field" type="text" name="name" placeholder="Name" aria-label="Name">
    <input class="field" type="email" name="email" placeholder="Email" aria-label="Email">
    <input class="field field-message" type="text" name="message" placeholder="Message" aria-label="Message">
    <button class="send" type="submit">Send</button>
  </form>

  <footer>
    <a class="abs social-dot" href="#" aria-label="Social media"></a>
    <p class="abs copyright">Copyright © 2022 Velmora - Cyber Threat Intelligence - Darknet and dark web - All Rights Reserved.</p>
    <p class="abs tagline">Not powered by the Darknet</p>
  </footer>
</body>
</html>
```